new roofing company card

New primary business card for roofing company.

Industry/Entity Type

Residential roofing/Specializing in Asphalt and Standing seam metal roofing

Contact Information for Business Card

Phone number is: 555 471 2086 Email: support@halvenshingleworks.example website: www.halvenshingleworks.example

Colors
EB3D1F
EC4F4E
F09395
F8D3D4
FCEDEE

```html
<!DOCTYPE html>
<html lang="en">
<head>
<meta charset="utf-8">
<title>Halven Shingleworks – Business Card</title>
<link rel="stylesheet" href="https://fonts.googleapis.com/css2?family=Cinzel:wght@400;600&family=Roboto:wght@400&display=swap">
<style>
  :root {
    --brand-red: #c03027;
    --ink: #262826;
    --paper: #ffffff;
    --backdrop: #6b6b6b;
    --back-card: #262826;
    --muted: #8a8c8a;
  }
  html, body {
    margin: 0;
    padding: 0;
    width: 1093px;
    height: 1200px;
    overflow: hidden;
    background: var(--backdrop);
  }
  .canvas {
    position: relative;
    width: 1093px;
    height: 1200px;
  }
  .card {
    position: absolute;
    left: 264px;
    width: 579px;
    height: 357px;
    overflow: hidden;
  }
  .card--front { top: 226px; background: var(--paper); }
  .card--back  { top: 620px; background: var(--back-card); }

  .front-shapes {
    position: absolute;
    inset: 0;
    width: 100%;
    height: 100%;
  }
  .holder {
    position: absolute;
    left: 26px;
    top: 52px;
    color: var(--paper);
  }
  .holder__name {
    font-family: "Cinzel", serif;
    font-weight: 600;
    font-size: 21px;
    letter-spacing: 0.5px;
    line-height: 1;
    margin: 0;
  }
  .holder__title {
    font-family: "Roboto", sans-serif;
    font-size: 16px;
    line-height: 1;
    margin: 3px 0 0;
  }
  .contact {
    position: absolute;
    left: 23px;
    top: 266px;
    margin: 0;
    padding: 0;
    list-style: none;
    font-family: "Roboto", sans-serif;
    font-size: 17px;
    color: var(--ink);
  }
  .contact__item {
    display: flex;
    align-items: center;
    height: 21px;
  }
  .contact__icon {
    width: 15px;
    height: 15px;
    margin-right: 8px;
    flex: none;
  }
  .contact__accent { color: var(--brand-red); }

  .wordmark {
    position: absolute;
    font-family: "Cinzel", serif;
    font-weight: 600;
    text-align: center;
    line-height: 1.05;
    margin: 0;
  }
  .wordmark--front {
    right: 22px;
    top: 130px;
    width: 250px;
    font-size: 30px;
    color: var(--ink);
  }
  .wordmark--back {
    left: 0;
    right: 0;
    top: 138px;
    font-size: 36px;
    color: var(--brand-red);
  }
</style>
</head>
<body>
<main class="canvas">

  <section class="card card--front" aria-label="Business card front">
    <svg class="front-shapes" viewBox="0 0 972 600" preserveAspectRatio="none" aria-hidden="true">
      <polygon fill="var(--brand-red)" points="0,0 972,0 972,23 538,23 432,210 0,210"/>
      <polygon fill="var(--ink)" points="546,31 972,31 972,58 532,58"/>
    </svg>

    <div class="holder">
      <p class="holder__name">MARCUS HALE</p>
      <p class="holder__title">Managing Director</p>
    </div>

    <p class="wordmark wordmark--front">HALVEN<br>SHINGLEWORKS</p>

    <ul class="contact">
      <li class="contact__item">
        <svg class="contact__icon" viewBox="0 0 24 24" aria-hidden="true">
          <path fill="var(--brand-red)" d="M6.6 10.8a15.1 15.1 0 0 0 6.6 6.6l2.2-2.2a1 1 0 0 1 1-.25 11.4 11.4 0 0 0 3.6.57 1 1 0 0 1 1 1V20a1 1 0 0 1-1 1A17 17 0 0 1 3 4a1 1 0 0 1 1-1h3.5a1 1 0 0 1 1 1c0 1.25.2 2.45.57 3.57a1 1 0 0 1-.25 1z"/>
        </svg>
        555 471 2086
      </li>
      <li class="contact__item">
        <svg class="contact__icon" viewBox="0 0 24 24" aria-hidden="true">
          <rect x="1" y="5" width="22" height="14" fill="var(--brand-red)"/>
          <polyline points="1,5 12,13 23,5" fill="none" stroke="var(--paper)" stroke-width="1.6"/>
        </svg>
        support@halvenshingleworks.example
      </li>
      <li class="contact__item">
        <svg class="contact__icon" viewBox="0 0 24 24" aria-hidden="true">
          <g fill="none" stroke="var(--brand-red)" stroke-width="1.8">
            <circle cx="12" cy="12" r="10"/>
            <ellipse cx="12" cy="12" rx="4.5" ry="10"/>
            <line x1="2" y1="12" x2="22" y2="12"/>
            <line x1="3.5" y1="7" x2="20.5" y2="7"/>
            <line x1="3.5" y1="17" x2="20.5" y2="17"/>
          </g>
        </svg>
        <span>www.<span class="contact__accent">halvenshingleworks</span>.example</span>
      </li>
    </ul>
  </section>

  <section class="card card--back" aria-label="Business card back">
    <p class="wordmark wordmark--back">HALVEN<br>SHINGLEWORKS</p>
  </section>

</main>
</body>
</html>
```